National Virtual accounting firm needs website designed

I need a wordpress website design for a national virtual accounting firm. I will upload my business card, logo, and postcards that I have had designed and followed the same style. I want a similar style to be followed so I can keep the running theme similar.

Services include:

Tax Services:
Tax preparation and planning services for Individuals, businesses, estates, and nonprofits
Full Service Payroll for Businesses
QVT Audit Representation

Consulting:
Entity Selection & Restructuring
Financial Projections & Forecasts
Retirement Planning
IPO Readiness

Accounting:
Bookkeeping
Reviews and Compilations
Payroll Services

Other Services:
CFO Services
Compliance Services
Controller Services
Software Implementations for Tenvolk, Brombalt, and Plovena.

Target Market(s)

small to medium size businesses, and individuals

Industry/Entity Type

accounting firms

Font styles to use
Sans Serif

Colors
59FF00
82FF00
B8FF75
E3FFCB
F4FFEA

Requirements
Must have
• Color schematics from the logo and post cards/business cards

```html
<!DOCTYPE html>
<html lang="en">
<head>
<meta charset="utf-8">
<title>Zenvoro — Advisors and Consultants</title>
<link href="https://fonts.googleapis.com/css2?family=Poppins:wght@400;500;600;700;800&display=swap" rel="stylesheet">
<style>
:root{
  --green:#45a83a;
  --green-dark:#2b8f3c;
  --green-light:#8cc63f;
  --yellow:#ffcc00;
  --ink:#2f2f33;
  --muted:#666;
  --footer:#3b3b3e;
  --white:#fff;
}
*{margin:0;padding:0;box-sizing:border-box}
html,body{width:1200px;height:4368px;overflow:hidden}
body{position:relative;font-family:'Poppins',sans-serif;color:var(--ink);background:var(--white)}
.abs{position:absolute}
.btn{position:absolute;background:var(--yellow);color:var(--ink);font-weight:700;font-size:12px;border-radius:30px;display:flex;align-items:center;justify-content:center;text-transform:uppercase}
.heading{position:absolute;left:0;width:1200px;text-align:center;font-weight:700;font-size:30px;letter-spacing:1px;text-transform:uppercase}
.heading::after{content:"";display:block;width:44px;height:2px;background:#ccc;margin:10px auto 0}
.photo{position:absolute}
.sun-glow{position:absolute;border-radius:50%;background:radial-gradient(closest-side,rgba(255,204,0,.6),rgba(255,204,0,.25) 55%,rgba(255,204,0,0))}

/* header */
.site-header{position:absolute;left:0;top:0;width:1200px;height:88px;background:var(--white)}
.brand{position:absolute;font-weight:800;color:var(--ink);display:flex;align-items:center;gap:10px}
.brand .dot{width:22px;height:22px;border-radius:50%;background:var(--yellow)}
.nav{position:absolute;left:432px;top:34px;display:flex;gap:35px;font-size:13px;font-weight:500;color:#444}
.nav .active{color:var(--green)}
.call{position:absolute;left:915px;top:22px;display:flex;align-items:center;gap:12px}
.call .ring{width:42px;height:42px;border-radius:50%;background:var(--green);display:flex;align-items:center;justify-content:center}
.call small{display:block;font-size:10px;font-weight:600}
.call strong{font-size:18px;font-weight:700}

/* hero */
.hero-title{position:absolute;left:0;top:318px;width:1200px;text-align:center;color:var(--white);font-weight:800;font-size:80px;line-height:76px;text-transform:uppercase;letter-spacing:1px}
.hero-sub{position:absolute;left:0;top:492px;width:1200px;text-align:center;color:var(--white);font-weight:700;font-size:20px}
.play{position:absolute;left:970px;top:787px;width:140px;height:140px;border-radius:50%;background:var(--white);box-shadow:0 8px 30px rgba(0,0,0,.15);display:flex;align-items:center;justify-content:center}

/* features */
.feature{position:absolute;top:905px;width:236px;text-align:center;font-weight:700;font-size:19px;letter-spacing:.5px}
.feature svg{display:block;margin:0 auto 22px}
.vline{position:absolute;top:905px;width:1px;height:105px;background:#ddd}

/* about */
.eyebrow{position:absolute;font-size:11px;font-weight:600;color:#888;text-transform:uppercase}
.about-title{position:absolute;left:650px;top:1187px;font-size:30px;font-weight:700}
.about-text{position:absolute;left:650px;top:1250px;width:385px;font-size:13px;line-height:22.3px;color:var(--muted)}

/* service cards */
.card{position:absolute;background:var(--white);box-shadow:0 6px 24px rgba(0,0,0,.08)}
.card h3{position:absolute;left:28px;font-size:17px;font-weight:700;text-transform:uppercase}
.card p{position:absolute;left:28px;width:265px;font-size:12.5px;line-height:19px;color:var(--muted)}
.card .more{position:absolute;left:28px;font-size:10px;font-weight:700;color:#999}

/* banner */
.banner-name{position:absolute;left:162px;top:2165px;font-size:112px;font-weight:800;color:var(--white);letter-spacing:2px;line-height:1}
.banner-sub{position:absolute;left:165px;top:2285px;font-size:26px;font-weight:700;color:var(--white);text-transform:uppercase}

/* working plan */
.step{position:absolute;top:2682px;width:120px;text-align:center;font-size:12px;font-weight:600;line-height:15px;text-transform:uppercase}
.step .disc{width:96px;height:96px;border-radius:50%;background:var(--white);box-shadow:0 6px 20px rgba(0,0,0,.1);margin:0 auto 14px;display:flex;align-items:center;justify-content:center}

/* blog */
.post h3{position:absolute;left:28px;top:272px;font-size:17px;font-weight:700;text-transform:uppercase}
.post .meta{position:absolute;left:28px;top:310px;font-size:10.5px;color:#888;display:flex;gap:22px}
.post p{position:absolute;left:28px;top:340px;width:270px;font-size:12px;line-height:19px;color:var(--muted)}

/* contact form */
.form-box{position:absolute;left:190px;top:3500px;width:447px;height:530px;background:var(--yellow)}
.field{position:absolute;background:var(--white);border-radius:22px;font-size:12px;color:#555;padding:13px 18px}
.submit{position:absolute;left:155px;top:373px;width:127px;height:37px;border-radius:20px;background:var(--ink);color:var(--white);font-weight:700;font-size:12px;display:flex;align-items:center;justify-content:center}
.chat-title{position:absolute;left:705px;top:3555px;font-size:35px;font-weight:700;line-height:44px;text-transform:uppercase}

/* footer */
.foot-h{position:absolute;top:4036px;font-size:16px;font-weight:700;color:var(--white);text-transform:uppercase}
.foot-links{position:absolute;left:453px;top:4090px;list-style:none;color:#ddd;font-size:12px;line-height:31.5px}
.foot-links li::before{content:"›";margin-right:8px;color:#999}
.contact-item{position:absolute;left:637px;color:#ddd;font-size:12px;line-height:17px;display:flex;gap:10px}
.contact-item span b{display:block;font-weight:500}
.copyright{position:absolute;top:4333px;font-size:12px;color:#ddd}
</style>
</head>
<body>

<header class="site-header">
  <div class="brand" style="left:90px;top:22px;font-size:34px"><span class="dot"></span>ZENVORO</div>
  <nav class="nav">
    <span class="active">HOME</span><span>ABOUT US</span><span>OUR SERVICES</span><span>BLOG</span><span>CONTACT US</span>
  </nav>
  <div class="call">
    <span class="ring"><svg width="20" height="20" viewBox="0 0 24 24"><path fill="#fff" d="M6.6 10.8a15 15 0 0 0 6.6 6.6l2.2-2.2c.3-.3.7-.4 1-.2 1.1.4 2.3.6 3.6.6.6 0 1 .4 1 1V20c0 .6-.4 1-1 1A17 17 0 0 1 3 4c0-.6.4-1 1-1h3.5c.6 0 1 .4 1 1 0 1.3.2 2.5.6 3.6.1.3 0 .7-.2 1z"/></svg></span>
    <div><small>CALL US:</small><strong>(555) 014-2387</strong></div>
  </div>
</header>

<section class="hero">
  <div class="photo" role="img" aria-label="Team of advisors gathered around a laptop in an office" style="left:0;top:88px;width:1200px;height:840px;background:linear-gradient(180deg,#3d3a3c 0%,#55504c 40%,#4a4644 75%,#6a6866 100%)"></div>
  <svg class="abs" style="left:0;top:760px" width="1200" height="200" viewBox="0 0 1200 200">
    <path d="M0 100 C 300 10, 700 0, 1200 110 L1200 200 L0 200Z" fill="var(--green-light)"/>
    <path d="M0 130 C 300 40, 700 30, 1200 150 L1200 200 L0 200Z" fill="var(--green)"/>
    <path d="M0 170 C 350 60, 750 50, 1200 200 L0 200Z" fill="#fff"/>
  </svg>
  <h1 class="hero-title">Advisors and<br>Consultants</h1>
  <p class="hero-sub">TAX PREPARATION AND PLANNING SERVICES</p>
  <div class="btn" style="left:480px;top:543px;width:240px;height:54px">Shedule a free consult now</div>
  <div class="play"><svg width="18" height="20"><path d="M2 1l15 9-15 9z" fill="#222"/></svg></div>
</section>

<section class="features">
  <div class="feature" style="left:249px"><svg width="70" height="64" viewBox="0 0 70 64" fill="none" stroke="#45a83a" stroke-width="2.5"><circle cx="28" cy="24" r="16"/><circle cx="28" cy="24" r="7"/><circle cx="52" cy="38" r="10"/><path d="M52 32v6l4 3M10 62c2-12 10-16 18-16s16 4 18 16"/></svg>EXPERIENCED</div>
  <div class="vline" style="left:485px"></div>
  <div class="feature" style="left:483px"><svg width="76" height="64" viewBox="0 0 76 64" fill="none" stroke="#45a83a" stroke-width="2.5"><circle cx="22" cy="14" r="7"/><circle cx="54" cy="14" r="7"/><circle cx="38" cy="22" r="7"/><path d="M8 38c2-10 26-10 28 0M40 38c2-10 26-10 28 0M4 40h68v20H4z"/></svg>PROFESSIONAL</div>
  <div class="vline" style="left:723px"></div>
  <div class="feature" style="left:719px"><svg width="76" height="64" viewBox="0 0 76 64" fill="none" stroke="#45a83a" stroke-width="2.5"><circle cx="44" cy="20" r="16"/><path d="M48 13h-6a3 3 0 0 0 0 7h4a3 3 0 0 1 0 7h-6M44 9v22M4 46l14-6h18l4 6H24M40 46l22-10 6 4-28 18H12"/></svg>AFFORDABLE</div>
</section>

<section class="about">
  <div class="sun-glow" role="img" aria-label="Yellow sunburst decoration" style="left:105px;top:1040px;width:330px;height:330px"></div>
  <div class="photo" role="img" aria-label="Colleagues reviewing documents together in an office" style="left:237px;top:1135px;width:370px;height:370px;border-radius:50%;background:linear-gradient(135deg,#8a7a70,#b7a9a0 50%,#5c6a7c);box-shadow:0 20px 40px rgba(0,0,0,.2)"></div>
  <p class="eyebrow" style="left:650px;top:1170px">Introduction</p>
  <h2 class="about-title">ABOUT ZENVORO</h2>
  <p class="about-text">There are many variations of passages the majority have suffered alteration in some fo injected randomised words believable. There are many variation passages the majority have suffered alteration in some fo injected humour, or randomised words believable. There are many variations of passages the majority have suffered alteration in some fo injected humour...</p>
  <div class="btn" style="left:650px;top:1427px;width:122px;height:39px">Read more</div>
</section>

<section class="services">
  <h2 class="heading" style="top:1568px">Our Services</h2>
  <div class="card" style="left:109px;top:1647px;width:321px;height:403px">
    <div class="photo" role="img" aria-label="Advisor and client reviewing tax documents" style="left:0;top:0;width:321px;height:253px;background:linear-gradient(135deg,#4b5260,#8d8e94 60%,#c9c7c2)"></div>
    <h3 style="top:275px">Tax Services</h3>
    <p style="top:308px">Lorem Ipsum is simply dummy text of the printing and typesetting..</p>
    <span class="more" style="top:362px">READ MORE</span>
  </div>
  <div class="card" style="left:440px;top:1647px;width:321px;height:403px">
    <div class="photo" role="img" aria-label="Consultants meeting around a table" style="left:0;top:0;width:321px;height:253px;background:linear-gradient(135deg,#3f4a3e,#7f8a78 55%,#b5b8a8)"></div>
    <h3 style="top:275px">Consulting</h3>
    <p style="top:308px">Lorem Ipsum is simply dummy text of the printing and typesetting..</p>
    <span class="more" style="top:362px">READ MORE</span>
  </div>
  <div class="card" style="left:771px;top:1647px;width:321px;height:403px">
    <div class="photo" role="img" aria-label="Accountants working together at a desk" style="left:0;top:0;width:321px;height:253px;background:linear-gradient(135deg,#b7b2ac,#d9d3cc 50%,#7b6f66)"></div>
    <h3 style="top:275px">Accounting</h3>
    <p style="top:308px">Lorem Ipsum is simply dummy text of the printing and typesetting..</p>
    <span class="more" style="top:362px">READ MORE</span>
  </div>
</section>

<section class="banner">
  <svg class="abs" style="left:0;top:2020px" width="1200" height="478" viewBox="0 0 1200 478">
    <defs><linearGradient id="bannerGrad" x1="0" y1="0" x2="1" y2="1"><stop offset="0" stop-color="#4cb848"/><stop offset="1" stop-color="#1f8a3f"/></linearGradient></defs>
    <path d="M0 150 C 40 60, 110 20, 160 20 L 0 20Z" fill="#e3f4d6"/>
    <path d="M0 200 C 60 60, 150 30, 200 30 C 500 30, 800 160, 1200 200 L1200 478 L0 478Z" fill="url(#bannerGrad)"/>
  </svg>
  <div class="banner-name">ZENVORO</div>
  <p class="banner-sub">National Virtual Accounting Firm</p>
  <div class="btn" style="left:165px;top:2336px;width:240px;height:52px">Shedule a free consult now</div>
  <div class="photo" role="img" aria-label="Two smiling business professionals in suits" style="left:700px;top:2130px;width:360px;height:368px;background:linear-gradient(180deg,rgba(60,60,60,0) 0%,#4a4a4a 35%,#2d2d2d 100%);border-radius:160px 160px 0 0;opacity:.9"></div>
</section>

<section class="plan">
  <div class="sun-glow" role="img" aria-label="Yellow sunburst decoration" style="left:170px;top:2555px;width:300px;height:280px"></div>
  <svg class="abs" style="left:330px;top:2700px" width="680" height="90" viewBox="0 0 680 90"><path d="M0 60 C 150 -10, 450 -10, 680 80 C 480 30, 200 20, 0 70Z" fill="var(--green-light)"/></svg>
  <h2 class="heading" style="top:2590px">Working Plan</h2>
  <div class="step" style="left:395px"><div class="disc"><svg width="46" height="46" viewBox="0 0 46 46" fill="none" stroke="#45a83a" stroke-width="2"><circle cx="20" cy="14" r="8"/><path d="M6 42c0-10 6-16 14-16s10 3 12 6M30 40l10-12 4 4-10 12h-4z"/></svg></div>Create an<br>Account</div>
  <div class="step" style="left:523px"><div class="disc"><svg width="46" height="46" viewBox="0 0 46 46" fill="none" stroke="#45a83a" stroke-width="2"><circle cx="13" cy="12" r="5"/><circle cx="33" cy="12" r="5"/><path d="M4 28c1-8 17-8 18 0M24 28c1-8 17-8 18 0M2 30h42M8 30v12M38 30v12"/></svg></div>Consult<br>with us</div>
  <div class="step" style="left:662px"><div class="disc"><svg width="46" height="46" viewBox="0 0 46 46" fill="none" stroke="#45a83a" stroke-width="2"><rect x="5" y="6" width="36" height="26" rx="2"/><path d="M11 14h24M11 20h24M11 26h14M18 32l-3 8h16l-3-8"/></svg></div>Fill up<br>the form</div>
  <div class="step" style="left:782px"><div class="disc"><svg width="46" height="46" viewBox="0 0 46 46" fill="none" stroke="#45a83a" stroke-width="2"><path d="M2 18l8-8 8 4 6-4 6 2 8-4 6 8-8 10-10 10-6-4-6-4-8-4z"/></svg></div>Get<br>started</div>
  <div class="abs" style="left:90px;top:2886px;width:1025px;height:1px;background:#e2e2e2"></div>
</section>

<section class="blog">
  <h2 class="heading" style="top:2935px">Latest Blog</h2>
  <div class="card post" style="left:115px;top:3005px;width:315px;height:395px">
    <div class="photo" role="img" aria-label="Team meeting around a laptop" style="left:0;top:0;width:315px;height:245px;background:linear-gradient(135deg,#2f3844,#5a6778 55%,#9aa0a8)"></div>
    <h3>Blog Heading Here</h3>
    <div class="meta"><span>▦ 25-05-2023</span><span>● By Mara</span></div>
    <p>Lorem Ipsum is simply printing typesetting industry lorem Ipsum...</p>
  </div>
  <div class="card post" style="left:443px;top:3005px;width:315px;height:395px">
    <div class="photo" role="img" aria-label="Colleagues discussing work at a desk" style="left:0;top:0;width:315px;height:245px;background:linear-gradient(135deg,#5a4a44,#8d7a70 50%,#c2b5a8)"></div>
    <h3>Blog Heading Here</h3>
    <div class="meta"><span>▦ 25-05-2023</span><span>● By Mara</span></div>
    <p>Lorem Ipsum is simply printing typesetting industry lorem Ipsum...</p>
  </div>
  <div class="card post" style="left:771px;top:3005px;width:315px;height:395px">
    <div class="photo" role="img" aria-label="Professionals reviewing a project together" style="left:0;top:0;width:315px;height:245px;background:linear-gradient(135deg,#3a3e44,#70747a 55%,#b5b1aa)"></div>
    <h3>Blog Heading Here</h3>
    <div class="meta"><span>▦ 25-05-2023</span><span>● By Mara</span></div>
    <p>Lorem Ipsum is simply printing typesetting industry lorem Ipsum...</p>
  </div>
</section>

<svg class="abs" style="left:0;top:3780px" width="1200" height="588" viewBox="0 0 1200 588">
  <path d="M0 190 C 300 40, 800 -10, 1200 50 L1200 588 L0 588Z" fill="var(--green-light)"/>
  <path d="M0 210 C 300 70, 800 20, 1200 75 L1200 588 L0 588Z" fill="var(--green)"/>
  <path d="M0 230 C 300 100, 800 55, 1200 100 L1200 588 L0 588Z" fill="var(--footer)"/>
</svg>

<section class="contact">
  <div class="form-box">
    <div class="field" style="left:53px;top:37px;width:165px;height:43px">First name</div>
    <div class="field" style="left:223px;top:37px;width:171px;height:43px">Last name</div>
    <div class="field" style="left:53px;top:90px;width:165px;height:43px">Phone</div>
    <div class="field" style="left:223px;top:90px;width:171px;height:43px">Email</div>
    <div class="field" style="left:53px;top:143px;width:341px;height:43px">Reference</div>
    <div class="field" style="left:53px;top:197px;width:341px;height:156px;border-radius:14px">Type your text</div>
    <div class="submit">SUBMIT</div>
  </div>
  <h2 class="chat-title">Let's chat tell<br>me about your<br>project</h2>
</section>

<footer>
  <div class="brand" style="left:90px;top:4105px;font-size:40px;color:var(--white)"><span class="dot"></span>ZENVORO</div>
  <h4 class="foot-h" style="left:453px">Quick Links</h4>
  <ul class="foot-links">
    <li>Home</li><li>About Us</li><li>Our Services</li><li>Blog</li><li>Our Careers</li><li>Contact Us</li>
  </ul>
  <h4 class="foot-h" style="left:637px">Contact Info</h4>
  <div class="contact-item" style="top:4090px"><span style="color:var(--green-light)">✉</span><span><b>Email:</b>hello@zenvoro.com</span></div>
  <div class="contact-item" style="top:4145px"><span style="color:var(--green-light)">✆</span><span><b>Phone:</b>(555) 014-2387</span></div>
  <div class="contact-item" style="top:4198px"><span style="color:var(--green-light)">◍</span><span><b>Web:</b>www.zenvoro.com</span></div>
  <h4 class="foot-h" style="left:853px">Newsletter</h4>
  <p class="abs" style="left:853px;top:4085px;width:230px;font-size:12px;line-height:17px;color:#ddd">Subscribe to our email address to get the latest news.</p>
  <div class="abs" style="left:853px;top:4138px;width:259px;height:47px;border-radius:24px;background:#4d4d51;color:#ddd;font-size:12px;display:flex;align-items:center;justify-content:space-between;padding:0 18px">
    <span>✉&nbsp; Enter Your Email...</span>
    <svg width="16" height="16" viewBox="0 0 16 16"><path d="M1 8l14-7-4 14-3-6z" fill="var(--green-light)"/></svg>
  </div>
  <div class="abs" style="left:90px;top:4310px;width:1025px;height:1px;background:#555"></div>
  <p class="copyright" style="left:483px">© Copyright 2023 All Rights Reserved</p>
  <p class="copyright" style="left:898px">Privacy Policy</p>
  <p class="copyright" style="left:998px">Terms &amp; Conditions</p>
  <div class="abs" style="left:1131px;top:4278px;width:44px;height:44px;border-radius:50%;background:var(--green);display:flex;align-items:center;justify-content:center">
    <svg width="14" height="14" viewBox="0 0 14 14"><path d="M7 12V2M3 6l4-4 4 4" stroke="#fff" stroke-width="1.8" fill="none"/></svg>
  </div>
</footer>

</body>
</html>
```